13 Tavo - new website design project

Our company Tavo Electrical is developing a new lead generation website focused on Electrical, LED Lighting and Solar Power. We need a high converting website.

Example of our current website is www.tavoelectrical.com.au You can take content from this website for this new design. Our colours are red, black and white. For our new website we would like to promote Tavo, Bright Days Ahead. Please listen to the jingle.

The below link is the company jingle that we have developed.
http://www.tunecraftaudio.com.au/tav-tc-v1/

The key for this brief is to generate leads for Electrical, LED Lighting (for commercial) and Solar Power & Storage.

Target Market(s)

Business owners in Melbourne Victoria

Number of Pages Required

4 page

Colors
ec1f27
ffffff

Requirements
Must have
• This page must be clean, be in line with company branding and a high converting lead website.

```html
<!DOCTYPE html>
<html lang="en">
<head>
<meta charset="utf-8">
<title>Tavo Electrical</title>
<link href="https://fonts.googleapis.com/css2?family=Open+Sans:wght@300;400;700&display=swap" rel="stylesheet">
<style>
  :root {
    --brand-red: #ec1f27;
    --ink: #2b2b2b;
    --white: #ffffff;
    --band: #231f20;
    --band-text: #e6e6e6;
  }
  * { box-sizing: border-box; margin: 0; padding: 0; }
  html, body {
    width: 1200px; height: 826px; overflow: hidden;
    background: var(--white);
    font-family: "Open Sans", Arial, sans-serif;
  }
  .page { position: relative; width: 1200px; height: 826px; }

  .site-header { position: absolute; left: 0; top: 0; width: 1200px; height: 142px; background: var(--white); }
  .brand { position: absolute; left: 50px; top: 36px; display: flex; align-items: center; gap: 12px; }
  .brand-dot { width: 22px; height: 22px; border-radius: 50%; background: var(--brand-red); }
  .brand-text { color: var(--ink); font-weight: 700; line-height: 1.1; }
  .brand-name { font-size: 44px; display: block; }
  .brand-tagline { font-size: 16px; display: block; }

  .main-nav { position: absolute; top: 54px; left: 0; width: 1200px; }
  .nav-link {
    position: absolute; font-size: 19px; font-weight: 400; color: var(--ink);
    text-decoration: none; letter-spacing: 0.2px; padding-bottom: 3px;
  }
  .nav-link.is-active { border-bottom: 2px solid var(--ink); }

  .hero { position: absolute; left: 0; top: 142px; width: 1200px; height: 480px; }
  .hero-art { position: absolute; inset: 0; }
  .service { position: absolute; top: 0; height: 480px; text-align: center; color: var(--white); }
  .service-title {
    position: absolute; top: 180px; left: 0; width: 100%;
    font-size: 35px; font-weight: 700; letter-spacing: 0.3px;
    text-shadow: 0 1px 3px rgba(0,0,0,0.35);
  }
  .service-button {
    position: absolute; top: 265px; left: 50%; transform: translateX(-50%);
    width: 241px; height: 55px; border: 2px solid var(--white);
    display: flex; align-items: center; justify-content: center;
    font-size: 18px; font-weight: 700; color: var(--white); text-decoration: none;
    text-shadow: 0 1px 2px rgba(0,0,0,0.3);
  }

  .intro-band {
    position: absolute; left: 0; top: 622px; width: 1200px; height: 204px;
    background: var(--band);
  }
  .intro-text {
    position: absolute; left: 50px; top: 60px; width: 1100px;
    text-align: center; color: var(--band-text);
    font-size: 19.5px; font-weight: 300; line-height: 25.5px;
  }
</style>
</head>
<body>
<div class="page">
  <header class="site-header">
    <div class="brand">
      <span class="brand-dot"></span>
      <span class="brand-text">
        <span class="brand-name">Tavo</span>
        <span class="brand-tagline">Bright Days Ahead</span>
      </span>
    </div>
    <nav class="main-nav">
      <a class="nav-link" href="#" style="left:678px">HOME</a>
      <a class="nav-link is-active" href="#" style="left:790px">OUR STORY</a>
      <a class="nav-link" href="#" style="left:937px">OUR WORK</a>
      <a class="nav-link" href="#" style="left:1090px">CONTACT</a>
    </nav>
  </header>

  <section class="hero">
    <svg class="hero-art" width="1200" height="480" viewBox="0 0 1200 480">
      <defs>
        <linearGradient id="wiresTone" x1="0" y1="0" x2="1" y2="1">
          <stop offset="0" stop-color="#d8c23a"/>
          <stop offset="0.35" stop-color="#d94a4a"/>
          <stop offset="0.65" stop-color="#3a6fd1"/>
          <stop offset="1" stop-color="#e0b820"/>
        </linearGradient>
        <linearGradient id="solarTone" x1="0" y1="0" x2="0" y2="1">
          <stop offset="0" stop-color="#2f6fc4"/>
          <stop offset="0.45" stop-color="#8fb6e0"/>
          <stop offset="0.7" stop-color="#2b4f8f"/>
          <stop offset="1" stop-color="#1c3566"/>
        </linearGradient>
        <linearGradient id="ledTone" x1="0" y1="0" x2="1" y2="0">
          <stop offset="0" stop-color="#5a2c6e"/>
          <stop offset="0.5" stop-color="#b24fb0"/>
          <stop offset="1" stop-color="#2a1436"/>
        </linearGradient>
      </defs>
      <polygon points="0,0 426,0 358,480 0,480" fill="url(#wiresTone)" role="img" aria-label="Photo of bundled red, yellow and blue electrical cables"/>
      <polygon points="426,0 843,0 777,480 358,480" fill="url(#solarTone)" role="img" aria-label="Photo of solar panels under a blue cloudy sky"/>
      <polygon points="843,0 1200,0 1200,480 777,480" fill="url(#ledTone)" role="img" aria-label="Close-up photo of a colourful LED light panel"/>
    </svg>

    <div class="service" style="left:0;width:378px">
      <h2 class="service-title">ELECTRICAL</h2>
      <a class="service-button" href="#">LEARN MORE</a>
    </div>
    <div class="service" style="left:395px;width:440px">
      <h2 class="service-title">SOLAR POWER</h2>
      <a class="service-button" href="#">LEARN MORE</a>
    </div>
    <div class="service" style="left:892px;width:300px">
      <h2 class="service-title">LED LIGHTING</h2>
      <a class="service-button" href="#">LEARN MORE</a>
    </div>
  </section>

  <section class="intro-band">
    <p class="intro-text">Tavo Electrical was formed to be an expert Electricity Contracting Company providing services to all Residential and Commercial Customers. With over 10 years of experience, Tavo Electrical has developed a highly-experienced team of professionals that ensure all our customer expectations are met.</p>
  </section>
</div>
</body>
</html>
```